Create a professional, eye-catching business card design that reflects the values and services of Brookfern Veterinary Hospital. we provide veterinary services and the business card should be a memorable representation of the clinic and align with its branding and mission. our tag line is "Gentle Hands for Every Stage of Life"
Use clean, modern typography. Prioritize readability and professionalism. We would like to see designs that use the color blue, as in the logo example. the final design should communicate professionalism and care, with attention to detail.

```html
<!DOCTYPE html>
<html lang="en">
<head>
<meta charset="UTF-8">
<title>Brookfern Veterinary Hospital – Business Card</title>
<link href="https://fonts.googleapis.com/css2?family=Montserrat:wght@400;500;700;800&display=swap" rel="stylesheet">
<style>
  :root {
    --navy: #1f3566;
    --navy-deep: #1a2d58;
    --navy-light: #34497a;
    --white: #ffffff;
    --paper: #ffffff;
    --backdrop: #e9eaee;
    --ink: #1f3566;
    --ink-soft: #263a63;
  }
  * { box-sizing: border-box; margin: 0; padding: 0; }
  html, body {
    width: 1200px; height: 900px; overflow: hidden;
    background: var(--backdrop);
    font-family: "Montserrat", sans-serif;
  }
  .stage {
    width: 1200px; height: 900px;
    display: flex; flex-direction: column;
    align-items: center; justify-content: center; gap: 40px;
  }
  .card {
    position: relative;
    width: 700px; height: 400px;
    border-radius: 22px;
    overflow: hidden;
    box-shadow: 0 10px 28px rgba(20, 30, 60, 0.25);
  }
  /* Front */
  .card-front {
    background: linear-gradient(115deg, var(--navy-deep) 0%, var(--navy) 55%, var(--navy-light) 100%);
    display: flex; align-items: center; justify-content: center;
  }
  .brand {
    display: flex; align-items: center; gap: 18px;
    color: var(--white);
    font-weight: 800;
    text-transform: uppercase;
  }
  .brand-mark {
    width: 74px; height: 74px; border-radius: 50%;
    border: 3px solid currentColor; flex-shrink: 0;
  }
  .brand-name { display: flex; flex-direction: column; line-height: 1; }
  .brand-name .primary { font-size: 58px; letter-spacing: 1px; }
  .brand-name .secondary { font-size: 20px; letter-spacing: 1.5px; margin-top: 6px; }

  /* Back */
  .card-back { background: var(--paper); color: var(--ink); }
  .card-back .wave { position: absolute; inset: 0; width: 100%; height: 100%; }
  .card-back .brand {
    position: absolute; top: 62px; right: 40px;
    color: var(--navy); gap: 12px;
  }
  .card-back .brand-mark { width: 48px; height: 48px; border-width: 2px; }
  .card-back .brand-name .primary { font-size: 38px; }
  .card-back .brand-name .secondary { font-size: 13px; margin-top: 4px; letter-spacing: 1px; }

  .contact { position: absolute; left: 44px; top: 48px; }
  .person-name { font-size: 27px; font-weight: 800; letter-spacing: 1px; text-transform: uppercase; }
  .person-title { font-size: 17px; font-weight: 500; margin-top: 4px; color: var(--ink-soft); }
  .address { margin-top: 28px; font-size: 17px; line-height: 1.4; color: var(--ink-soft); }
  .details { margin-top: 24px; list-style: none; font-size: 17px; color: var(--ink-soft); }
  .details li { display: flex; align-items: center; gap: 10px; line-height: 1.55; }
  .details svg { width: 16px; height: 16px; flex-shrink: 0; fill: var(--navy); }

  .tagline {
    position: absolute; right: 36px; bottom: 26px;
    color: var(--white); font-size: 18px; font-weight: 500; letter-spacing: 0.3px;
  }
</style>
</head>
<body>
<main class="stage">
  <section class="card card-front" aria-label="Business card front">
    <div class="brand">
      <span class="brand-mark" aria-hidden="true"></span>
      <div class="brand-name">
        <span class="primary">Brookfern</span>
        <span class="secondary">Veterinary Hospital</span>
      </div>
    </div>
  </section>

  <section class="card card-back" aria-label="Business card back">
    <svg class="wave" viewBox="0 0 700 400" preserveAspectRatio="none" aria-hidden="true">
      <path d="M0,400 L0,372 C180,372 320,340 430,276 C530,218 610,190 700,176 L700,400 Z" fill="var(--navy)"/>
      <path d="M0,352 C170,352 300,322 400,262 C470,220 520,206 560,202" fill="none" stroke="var(--navy)" stroke-width="3"/>
    </svg>

    <div class="brand">
      <span class="brand-mark" aria-hidden="true"></span>
      <div class="brand-name">
        <span class="primary">Brookfern</span>
        <span class="secondary">Veterinary Hospital</span>
      </div>
    </div>

    <div class="contact">
      <h1 class="person-name">Daniel Marsh</h1>
      <p class="person-title">Managing Director</p>
      <p class="address">Your address, City<br>State, Zip 1234</p>
      <ul class="details">
        <li>
          <svg viewBox="0 0 24 24" aria-hidden="true"><path d="M6.6 10.8a15.1 15.1 0 0 0 6.6 6.6l2.2-2.2a1 1 0 0 1 1-.25 11.4 11.4 0 0 0 3.6.57 1 1 0 0 1 1 1V20a1 1 0 0 1-1 1A17 17 0 0 1 3 4a1 1 0 0 1 1-1h3.5a1 1 0 0 1 1 1c0 1.25.2 2.450.57 3.6a1 1 0 0 1-.25 1z"/></svg>
          123 456 789
        </li>
        <li>
          <svg viewBox="0 0 24 24" aria-hidden="true"><path d="M3 5h18a1 1 0 0 1 1 1v12a1 1 0 0 1-1 1H3a1 1 0 0 1-1-1V6a1 1 0 0 1 1-1zm9 7.2L4 7v1.3l8 5.2 8-5.2V7z"/></svg>
          info@brookfernvet.com
        </li>
        <li>
          <svg viewBox="0 0 24 24" aria-hidden="true"><path d="M12 2a10 10 0 1 0 0 20 10 10 0 0 0 0-20zm6.9 6h-2.9a15.7 15.7 0 0 0-1.4-3.6A8 8 0 0 1 18.9 8zM12 4c.8 1.2 1.5 2.5 1.9 4h-3.8c.4-1.5 1.1-2.8 1.9-4zM4.3 14a8.2 8.2 0 0 1 0-4h3.4a16 16 0 0 0 0 4zm.8 2h2.9c.3 1.3.8 2.5 1.4 3.6A8 8 0 0 1 5.1 16zM8 8H5.1a8 8 0 0 1 4.3-3.6C8.8 5.5 8.3 6.7 8 8zm4 12c-.8-1.2-1.5-2.5-1.9-4h3.8c-.4 1.5-1.1 2.8-1.9 4zm2.3-6H9.7a14.7 14.7 0 0 1 0-4h4.6a14.7 14.7 0 0 1 0 4zm.3 5.6c.6-1.1 1.1-2.3 1.4-3.6h2.9a8 8 0 0 1-4.3 3.6zM16.3 14a16 16 0 0 0 0-4h3.4a8.2 8.2 0 0 1 0 4z"/></svg>
          www.brookfernvet.com
        </li>
      </ul>
    </div>

    <p class="tagline">Gentle Hands for Every Stage of Life</p>
  </section>
</main>
</body>
</html>
```